KM PowerPoint Design

I need a slick PowerPoint template following my newly designed logo (see the attached ZIP file for logo details, fonts, and colors).
Please also see the Sample.pptx file for an idea of the simplicity and slickness I am after (do not consider the colors or fonts from the Sample file, just as an idea). Other ideas are very welcome.

```html
<!DOCTYPE html>
<html lang="en">
<head>
<meta charset="utf-8">
<title>KM Course Presentation Template</title>
<link href="https://fonts.googleapis.com/css2?family=Montserrat:wght@400;600;700;800&family=Open+Sans:wght@400;600;700&display=swap" rel="stylesheet">
<style>
:root{
  --purple:#4b2378;
  --ink:#2a1f3d;
  --teal:#3aa891;
  --green:#5cb88a;
  --blue:#1aa5e0;
  --red:#e8574a;
  --orange:#e8602c;
  --navy:#0d1a6b;
  --gold:#f2b21c;
  --grey:#8a8a8a;
  --paper:#ffffff;
  --mist:#f1f1f3;
  --gap:#e4e4e7;
}
*{margin:0;padding:0;box-sizing:border-box}
html,body{width:1200px;height:4800px;overflow:hidden;background:var(--gap)}
body{font-family:"Open Sans",Arial,sans-serif;color:var(--ink)}
.slide{position:absolute;left:0;width:1200px;height:675px;background:var(--paper);overflow:hidden}
.abs{position:absolute}
.photo{position:absolute}
.h-title{font-family:"Montserrat",Arial,sans-serif;font-weight:800;color:var(--ink);font-size:40px;line-height:1.05}
.label{font-family:"Montserrat",sans-serif;font-weight:700;font-size:18px;color:var(--ink)}
.kicker{font-family:"Montserrat",sans-serif;font-weight:700;font-size:18px;color:var(--orange)}
.body{font-size:14px;line-height:1.7;color:var(--grey)}
.brand{font-family:"Montserrat",sans-serif;font-weight:800;color:var(--purple);display:flex;align-items:center;justify-content:center}
.brand-circle{border-radius:50%;border:6px solid var(--purple);display:flex;align-items:center;justify-content:center}
/* cover */
.cover-title{font-family:"Montserrat",sans-serif;font-weight:800;font-size:58px;color:var(--ink);width:560px;text-align:center}
.cover-sub{font-size:28px;color:var(--ink);width:560px;text-align:center}
/* contents */
.toc-bar{width:56px;height:8px;background:var(--purple)}
.toc-head{font-family:"Montserrat",sans-serif;font-size:40px;font-weight:600;color:var(--ink)}
.toc-head span{color:var(--teal);font-weight:700}
.toc-item{position:absolute;width:360px;display:flex;gap:14px}
.toc-num{font-family:"Montserrat",sans-serif;font-size:36px;font-weight:600;color:var(--ink);line-height:1}
.toc-name{font-family:"Montserrat",sans-serif;font-size:26px;font-weight:700;color:var(--teal);line-height:1}
.toc-desc{font-size:15px;line-height:1.6;color:var(--ink);margin-top:8px}
/* badges */
.badge{position:absolute;border-radius:16px;color:#fff;font-family:"Montserrat",sans-serif;text-align:center;padding-top:14px;box-shadow:0 6px 14px rgba(0,0,0,.15)}
.badge b{display:block;font-size:34px;font-weight:700;line-height:1.1}
.badge span{font-size:16px;font-weight:600}
.pill{position:absolute;width:160px;border-radius:80px}
/* progress */
.bar{position:absolute;left:592px;width:448px;height:26px;border-radius:13px;background:#d9d9dd}
.bar-fill{height:26px;border-radius:13px;color:#fff;font-size:13px;font-weight:600;display:flex;justify-content:space-between;align-items:center;padding:0 14px}
.stars{color:var(--gold);font-size:30px;letter-spacing:4px}
</style>
</head>
<body>

<!-- Cover -->
<section class="slide" style="top:0">
  <div class="photo" role="img" aria-label="Smiling student holding folders and a backpack" style="left:0;top:0;width:520px;height:660px;background:linear-gradient(160deg,#f4efe9,#d9b59a 45%,#e7b83a 70%,#f3f0ee)"></div>
  <div class="abs brand" style="left:760px;top:120px;width:200px;height:240px">
    <div class="brand-circle" style="width:200px;height:200px;font-size:72px">KM</div>
  </div>
  <div class="abs cover-title" style="left:580px;top:410px">Course 01</div>
  <div class="abs cover-sub" style="left:580px;top:490px">Insert text here</div>
</section>

<!-- Contents -->
<section class="slide" style="top:687px">
  <div class="abs toc-bar" style="left:80px;top:90px"></div>
  <div class="abs toc-head" style="left:80px;top:110px">LIST OF <span>CONTENT</span></div>
  <div class="toc-item" style="left:80px;top:228px"><div class="toc-num">01.</div><div><div class="toc-name">ABOUT US</div><div class="toc-desc">Suitable for all categories business and personal presentation</div></div></div>
  <div class="toc-item" style="left:460px;top:228px"><div class="toc-num">02.</div><div><div class="toc-name">Purpose &amp; Goals</div><div class="toc-desc">Suitable for all categories business and personal presentation</div></div></div>
  <div class="toc-item" style="left:832px;top:228px"><div class="toc-num">03.</div><div><div class="toc-name">Our Mission</div><div class="toc-desc">Suitable for all categories business and personal presentation</div></div></div>
  <div class="toc-item" style="left:80px;top:362px"><div class="toc-num">04.</div><div><div class="toc-name">CHART</div><div class="toc-desc">Suitable for all categories business and personal presentation</div></div></div>
  <div class="toc-item" style="left:460px;top:362px"><div class="toc-num">05.</div><div><div class="toc-name">TESTIMONIAL</div><div class="toc-desc">Suitable for all categories business and personal presentation</div></div></div>
  <div class="toc-item" style="left:832px;top:362px"><div class="toc-num">06.</div><div><div class="toc-name">CONTACT</div><div class="toc-desc">Suitable for all categories business and personal presentation</div></div></div>
  <div class="toc-item" style="left:80px;top:496px"><div class="toc-num">07.</div><div><div class="toc-name">ABOUT US</div><div class="toc-desc">Suitable for all categories business and personal presentation</div></div></div>
  <div class="toc-item" style="left:460px;top:496px"><div class="toc-num">08.</div><div><div class="toc-name">OUR TEAM</div><div class="toc-desc">Suitable for all categories business and personal presentation</div></div></div>
  <div class="toc-item" style="left:832px;top:496px"><div class="toc-num">09.</div><div><div class="toc-name">GALLERY</div><div class="toc-desc">Suitable for all categories business and personal presentation</div></div></div>
</section>

<!-- Investment -->
<section class="slide" style="top:1374px">
  <div class="photo" role="img" aria-label="Student with headphones holding a red binder against a wooden wall" style="left:0;top:0;width:540px;height:675px;background:linear-gradient(135deg,#8a5a36,#c79367 40%,#d8404a 65%,#6b4a30)"></div>
  <div class="abs h-title" style="left:620px;top:120px;width:500px">An investment in knowledge pays the best interest</div>
  <div class="abs label" style="left:620px;top:272px">Insert text here</div>
  <p class="abs body" style="left:620px;top:306px;width:500px">Our course blends practical lessons with steady mentoring so every learner builds skill, confidence and clear goals. Each module closes with a short review and a guided project.</p>
  <p class="abs body" style="left:620px;top:420px;width:500px">Small groups and weekly feedback keep progress visible and help students turn knowledge into lasting results.</p>
</section>

<!-- About -->
<section class="slide" style="top:2061px;background:var(--mist)">
  <svg class="abs" style="left:0;top:0" width="1200" height="675"><polygon points="0,0 780,0 300,675 0,675" fill="#fff"/></svg>
  <div class="abs kicker" style="left:72px;top:132px">About Our Course</div>
  <div class="abs h-title" style="left:72px;top:162px;width:520px;color:var(--purple);font-size:36px">Education is the passport to the future, for tomorrow belongs to those who prepare for it today</div>
  <p class="abs body" style="left:72px;top:350px;width:480px">Our course blends practical lessons with steady mentoring so every learner builds skill and confidence.</p>
  <p class="abs body" style="left:72px;top:430px;width:480px">Weekly feedback keeps progress visible for every student.</p>
  <div class="pill" role="img" aria-label="Students studying together at a table" style="left:652px;top:100px;height:480px;background:linear-gradient(180deg,#c9a68a,#8b6a58)"></div>
  <div class="pill" role="img" aria-label="Teacher helping a student at a laptop" style="left:824px;top:60px;height:560px;background:linear-gradient(180deg,#d9c3ae,#b87a5a)"></div>
  <div class="pill" role="img" aria-label="Student writing notes in class" style="left:996px;top:20px;height:520px;background:linear-gradient(180deg,#a8b2b5,#d87a46)"></div>
  <div class="badge" style="left:560px;top:52px;width:240px;height:104px;background:var(--blue)"><b>240</b><span>Happy Students</span></div>
  <div class="badge" style="left:912px;top:524px;width:150px;height:104px;background:var(--green)"><b>12</b><span>Curriculum</span></div>
</section>

<!-- Stats -->
<section class="slide" style="top:2748px">
  <div class="abs" style="left:0;top:400px;width:1200px;height:275px;background:var(--mist)"></div>
  <div class="photo" role="img" aria-label="Student with glasses studying among colourful books" style="left:0;top:40px;width:540px;height:360px;background:linear-gradient(135deg,#f3ead8,#e6b45c 45%,#d96a4a 75%,#efe2cf)"></div>
  <div class="badge" style="left:24px;top:440px;width:180px;height:116px;background:var(--blue)"><b>240</b><span>Happy Students</span></div>
  <div class="badge" style="left:228px;top:440px;width:160px;height:116px;background:var(--green)"><b>12</b><span>Curriculum</span></div>
  <div class="badge" style="left:400px;top:440px;width:160px;height:116px;background:var(--red)"><b>450</b><span>Awards</span></div>
  <div class="abs h-title" style="left:592px;top:56px;width:420px">An investment in knowledge pays the best interest</div>
  <div class="abs brand" style="left:1040px;top:50px"><div class="brand-circle" style="width:100px;height:100px;font-size:36px;border-width:4px">KM</div></div>
  <div class="abs kicker" style="left:592px;top:200px">About Our Course</div>
  <p class="abs body" style="left:592px;top:232px;width:480px">Our course blends practical lessons with steady mentoring so every learner builds skill and confidence step by step.</p>
  <div class="bar" style="top:424px"><div class="bar-fill" style="width:76%;background:var(--green)"><span>Insert text here</span><span>76%</span></div></div>
  <div class="bar" style="top:476px"><div class="bar-fill" style="width:75%;background:var(--red)"><span>Insert text here</span><span>75%</span></div></div>
  <div class="bar" style="top:524px"><div class="bar-fill" style="width:80%;background:var(--blue)"><span>Insert text here</span><span>80%</span></div></div>
</section>

<!-- Passport -->
<section class="slide" style="top:3435px">
  <div class="abs" style="left:0;top:0;width:1200px;height:280px;background:var(--purple)"></div>
  <div class="abs h-title" style="left:128px;top:96px;width:560px;color:#fff;font-size:36px">Education is the passport to the future, for tomorrow belongs to those who prepare for it today</div>
  <p class="abs body" style="left:128px;top:300px;width:540px">Our course blends practical lessons with steady mentoring so every learner builds skill and confidence. Weekly feedback keeps progress visible and helps turn knowledge into results.</p>
  <div class="abs label" style="left:128px;top:420px">01. Insert text here</div>
  <p class="abs body" style="left:128px;top:450px;width:230px">Short lessons and guided tasks help you practise every day.</p>
  <div class="abs stars" style="left:128px;top:540px">★★★★<span style="color:#d0d0d0">★</span></div>
  <div class="abs label" style="left:392px;top:420px;color:var(--teal)">02. Insert text here</div>
  <p class="abs body" style="left:392px;top:450px;width:230px">Short lessons and guided tasks help you practise every day.</p>
  <div class="abs stars" style="left:392px;top:540px">★★★★<span style="color:#d0d0d0">★</span></div>
  <div class="photo" role="img" aria-label="Two students smiling in a bright window-lit room" style="left:740px;top:220px;width:460px;height:400px;background:linear-gradient(135deg,#eef0f2,#c9cdd3 50%,#8a7a6e)"></div>
  <div class="abs" style="left:740px;top:500px;width:340px;height:120px;background:var(--navy);border-radius:16px;color:#fff;text-align:center;padding-top:24px">
    <div style="font-family:Montserrat,sans-serif;font-weight:700;font-size:18px">Insert text here</div>
    <div style="font-size:14px;margin-top:10px;opacity:.85">Clear steps for every learner.</div>
  </div>
</section>

<!-- Gallery -->
<section class="slide" style="top:4122px">
  <div class="photo" role="img" aria-label="Students in a lecture hall" style="left:20px;top:0;width:200px;height:260px;border-radius:24px;background:linear-gradient(160deg,#7a7f84,#3f4448)"></div>
  <div class="photo" role="img" aria-label="Student working on a laptop" style="left:20px;top:280px;width:200px;height:360px;border-radius:24px;background:linear-gradient(160deg,#b9c3c9,#5a6670)"></div>
  <div class="photo" role="img" aria-label="Smiling student holding books" style="left:236px;top:40px;width:180px;height:560px;border-radius:24px;background:linear-gradient(180deg,#6a5a50,#c48a6a)"></div>
  <div class="photo" role="img" aria-label="Student with glasses reading" style="left:432px;top:60px;width:190px;height:260px;border-radius:24px;background:linear-gradient(160deg,#cfcac4,#6e6660)"></div>
  <div class="photo" role="img" aria-label="Students collaborating at a desk" style="left:432px;top:340px;width:190px;height:300px;border-radius:24px;background:linear-gradient(160deg,#9a7a5e,#4c3a2c)"></div>
  <div class="abs h-title" style="left:688px;top:100px;width:460px">An investment in knowledge pays the best interest</div>
  <div class="abs label" style="left:688px;top:256px">Insert text here</div>
  <p class="abs body" style="left:688px;top:288px;width:470px">Our course blends practical lessons with steady mentoring so every learner builds skill and confidence. Weekly feedback keeps progress visible.</p>
  <div class="photo" role="img" aria-label="Portrait of the course teacher" style="left:740px;top:430px;width:90px;height:90px;border-radius:50%;background:linear-gradient(160deg,#6b5a52,#2c2420)"></div>
  <div class="abs" style="left:848px;top:432px;width:300px;font-size:14px;line-height:1.5;color:var(--ink)">"Education is what remains after one has forgotten what one has learned in school"</div>
  <div class="abs" style="left:848px;top:510px;font-size:14px;color:var(--ink)"><b>Marla Quinn</b> | Teacher of Course</div>
</section>

</body>
</html>
```